Google slides for an upcoming presentation

I would like to recreate the jpeg to better match our company branding & color, as well as better resolution-- which is found in the PPTX. The slide should read....
"What are the biggest differences between Web 2.0 to Web 3.0"

Industry/Entity Type

Web3

Other font styles liked:
• Manrope

```html
<!DOCTYPE html>
<html lang="en">
<head>
<meta charset="utf-8">
<title>Web 2.0 to Web 3.0</title>
<link rel="stylesheet" href="https://fonts.googleapis.com/css2?family=Sora:wght@400;700;800&display=swap">
<style>
  :root {
    --ink: #232126;
    --numeral: #433f42;
    --accent-blue: #6ea0f5;
    --ring-teal: #7cc8d8;
    --ring-violet: #b98ae0;
    --ring-pink: #d77ad8;
    --bg-slate: #b4bfd2;
    --bg-rose: #dcc4cc;
    --bg-tan: #bba894;
    --bg-sky: #9cc6ea;
    --bg-sand: #c8ab9c;
    --bg-white: #ffffff;
  }
  * { margin: 0; padding: 0; box-sizing: border-box; }
  html, body { width: 1200px; height: 847px; overflow: hidden; }
  body { font-family: "Sora", sans-serif; }

  .slide {
    position: relative;
    width: 1200px;
    height: 847px;
    overflow: hidden;
    background:
      radial-gradient(ellipse 260px 200px at 1120px 790px, var(--bg-white) 0%, rgba(255,255,255,0) 100%),
      radial-gradient(ellipse 360px 220px at 760px 840px, rgba(156,198,234,0.95) 0%, rgba(156,198,234,0) 100%),
      radial-gradient(ellipse 420px 300px at 1200px 0px, rgba(187,168,148,0.95) 0%, rgba(187,168,148,0) 100%),
      radial-gradient(ellipse 300px 260px at 0px 847px, rgba(200,171,156,0.9) 0%, rgba(200,171,156,0) 100%),
      radial-gradient(ellipse 520px 360px at 760px 380px, rgba(228,208,222,0.9) 0%, rgba(228,208,222,0) 100%),
      linear-gradient(100deg, var(--bg-slate) 0%, var(--bg-rose) 60%, #e6d4cc 100%);
  }

  .headline {
    position: absolute;
    left: 135px;
    top: 128px;
    font-size: 36px;
    font-weight: 400;
    color: var(--ink);
    letter-spacing: 0.2px;
    white-space: nowrap;
  }
  .headline strong { font-weight: 700; }

  .web-word, .to-word {
    position: absolute;
    color: var(--accent-blue);
    font-weight: 800;
    line-height: 1;
    text-align: center;
    width: 400px;
    left: 400px;
  }
  .web-word { top: 313px; font-size: 96px; letter-spacing: -3px; }
  .to-word { top: 538px; font-size: 96px; letter-spacing: -2px; }

  .version {
    position: absolute;
    width: 270px;
    height: 270px;
    top: 330px;
  }
  .version--from { left: 125px; }
  .version--to { left: 802px; }
  .version svg { position: absolute; inset: 0; }
  .version-number {
    position: absolute;
    inset: 0;
    display: flex;
    align-items: center;
    justify-content: center;
    font-size: 82px;
    font-weight: 700;
    color: var(--numeral);
    letter-spacing: -1px;
  }
</style>
</head>
<body>
<main class="slide">
  <h1 class="headline">What are the <strong>biggest differences</strong> between</h1>

  <div class="web-word">WEB</div>
  <div class="to-word">to</div>

  <div class="version version--from">
    <svg viewBox="0 0 270 270" role="img" aria-label="Ring of rotated line squares in teal to violet around the version number">
      <defs>
        <linearGradient id="ringFromGrad" x1="0" y1="0" x2="1" y2="0">
          <stop offset="0" stop-color="var(--ring-teal)"/>
          <stop offset="0.5" stop-color="var(--ring-violet)"/>
          <stop offset="1" stop-color="var(--ring-pink)"/>
        </linearGradient>
      </defs>
      <circle cx="135" cy="135" r="113" fill="none" stroke="url(#ringFromGrad)" stroke-width="38" opacity="0.28"/>
      <circle cx="135" cy="135" r="94" fill="none" stroke="url(#ringFromGrad)" stroke-width="1.4"/>
    </svg>
    <div class="version-number">2.0</div>
  </div>

  <div class="version version--to">
    <svg viewBox="0 0 270 270" role="img" aria-label="Dense ring of rotated line squares in teal to pink around the version number">
      <defs>
        <linearGradient id="ringToGrad" x1="0" y1="0" x2="1" y2="0">
          <stop offset="0" stop-color="var(--ring-teal)"/>
          <stop offset="0.5" stop-color="var(--ring-violet)"/>
          <stop offset="1" stop-color="var(--ring-pink)"/>
        </linearGradient>
      </defs>
      <circle cx="135" cy="135" r="113" fill="none" stroke="url(#ringToGrad)" stroke-width="38" opacity="0.28"/>
      <circle cx="135" cy="135" r="94" fill="none" stroke="url(#ringToGrad)" stroke-width="1.4"/>
    </svg>
    <div class="version-number">3.0</div>
  </div>
</main>
</body>
</html>
```